Business Card Design

Need business card design for all carpentry & construction solutions. We would like to see designs that use black as a background with orange writing as it would stand out.

Business

KRV CONTRACTING
MARTIN COLBY
14 PELLINGTON ST
WONGAN HILLS
WA 6603
0498371265
krvcontracting@tramlex.com

```html
<!DOCTYPE html>
<html lang="en">
<head>
<meta charset="utf-8">
<title>KRV Contracting – Business Card</title>
<link rel="stylesheet" href="https://fonts.googleapis.com/css2?family=Oswald:wght@500&family=Open+Sans:wght@400;600&display=swap">
<style>
  :root {
    --stage: #1c1a19;
    --card-front: #0c0c0c;
    --card-back: #151816;
    --orange: #f26a2e;
    --ink-light: #c9c9c9;
    --ink-soft: #9a9a9a;
    --emboss: #262626;
    --divider: #4a4c4a;
  }
  * { margin: 0; padding: 0; box-sizing: border-box; }
  html, body { width: 1200px; height: 716px; overflow: hidden; background: var(--stage); }
  .stage {
    position: relative; width: 1200px; height: 716px;
    display: flex; align-items: center; justify-content: center; gap: 60px;
  }
  .card {
    width: 510px; height: 292px; position: relative;
    box-shadow: 0 10px 30px rgba(0,0,0,.55);
  }
  .card--front {
    background: var(--card-front);
    display: flex; align-items: center; justify-content: center;
  }
  .front-name {
    font-family: "Oswald", sans-serif; font-weight: 500;
    font-size: 40px; letter-spacing: 2px; color: var(--emboss);
  }
  .card--back { background: var(--card-back); display: flex; align-items: center; }
  .brand {
    width: 250px; flex-shrink: 0; display: flex; align-items: center; justify-content: center; gap: 10px;
  }
  .brand-mark { width: 14px; height: 14px; background: var(--orange); }
  .brand-name {
    font-family: "Oswald", sans-serif; font-weight: 500;
    font-size: 24px; letter-spacing: 1px; color: var(--orange); white-space: nowrap;
  }
  .divider { width: 1px; height: 150px; background: var(--divider); flex-shrink: 0; }
  .details { padding-left: 36px; font-family: "Open Sans", sans-serif; white-space: nowrap; }
  .person-name {
    font-family: "Oswald", sans-serif; font-weight: 500;
    font-size: 16px; letter-spacing: 1px; color: var(--orange);
  }
  .person-role { font-size: 11px; font-weight: 600; color: var(--ink-light); margin-bottom: 10px; }
  .contact { display: flex; align-items: center; gap: 8px; font-size: 12px; color: var(--ink-soft); margin-bottom: 4px; }
  .contact-icon { width: 12px; height: 12px; background: var(--orange); border-radius: 2px; display: flex; align-items: center; justify-content: center; }
  .address { margin-top: 8px; font-size: 11.5px; font-weight: 600; color: var(--ink-light); line-height: 1.45; }
</style>
</head>
<body>
<main class="stage">
  <section class="card card--front">
    <span class="front-name">KRV CONTRACTING</span>
  </section>

  <section class="card card--back">
    <div class="brand">
      <span class="brand-mark"></span>
      <span class="brand-name">KRV CONTRACTING</span>
    </div>
    <div class="divider"></div>
    <div class="details">
      <p class="person-name">MARTIN COLBY</p>
      <p class="person-role">MANAGING DIRECTOR</p>
      <p class="contact">
        <span class="contact-icon">
          <svg width="8" height="8" viewBox="0 0 24 24"><path fill="#151816" d="M6.6 10.8a15 15 0 0 0 6.6 6.6l2.2-2.2c.3-.3.7-.4 1-.2 1.1.4 2.3.6 3.6.6.6 0 1 .4 1 1V20c0 .6-.4 1-1 1A17 17 0 0 1 3 4c0-.6.4-1 1-1h3.5c.6 0 1 .4 1 1 0 1.3.2 2.5.6 3.6.1.3 0 .7-.2 1z"/></svg>
        </span>
        0498371265
      </p>
      <p class="contact">
        <span class="contact-icon">
          <svg width="8" height="8" viewBox="0 0 24 24"><path fill="#151816" d="M2 5h20v14H2z M2 5l10 8 10-8" stroke="#f26a2e" stroke-width="1.5"/></svg>
        </span>
        krvcontracting@tramlex.com
      </p>
      <p class="address">14 PELLINGTON ST<br>MARLOWE HILLS, WA 6712</p>
    </div>
  </section>
</main>
</body>
</html>
```